Help me design my in store poster to promote our Loan product!

We need a design for a 2 X 3 poster inside our stores to promote our installment loan product. We are called Wade's Check Cashing, but offer loans inside our stores. We are open to a new logo for Wade's Loans, and open to any new exciting colors to stand out in the store. We provide short term monthly installment loans, we have monthly payments from 3 - 12 months. Our loans range from $100 - $1,400 with low interest. We ask for ID, consistent source of income, and credit check. We help build credit, and it is fast and easy. We want it to be simple and clean to get people's attention when they are inside our stores. Please help!

UPDATE: The design will be for a 2 X 7 poster now. Less words.

Other font styles liked:
• Rounded corners with the font

Requirements
Must have
• Bold colors, the words: loans, cash, $100 - $1,400, monthly payments, credit building, quick.
Nice to have
• A new logo, the Wade's Check Cashing logo added as reference

UPDATE: If we can add a quick slogan : FAST CASH NOW or HELP IS HERE or YOUR CASH IS HERE or LOANS FOR LIVING or LOANS FOR LIFE

A WADE'S FINANCE LOGO that looks similar to the NOVAJET logo I attached.

```html
<!DOCTYPE html>
<html lang="en">
<head>
<meta charset="utf-8">
<title>Wade's Check Cashing – Loans Poster</title>
<link href="https://fonts.googleapis.com/css2?family=Poppins:wght@200;500;800;900&display=swap" rel="stylesheet">
<style>
  :root {
    --brand-blue: #0b55a3;
    --brand-navy: #1e3d70;
    --paper: #ffffff;
  }
  html, body {
    margin: 0;
    padding: 0;
    width: 800px;
    height: 1200px;
    overflow: hidden;
    background: var(--paper);
  }
  .poster {
    position: relative;
    width: 800px;
    height: 1200px;
    font-family: "Poppins", sans-serif;
  }
  .poster svg { display: block; }
  .brand-name { fill: var(--brand-blue); font-weight: 800; }
  .brand-mark { fill: var(--brand-blue); }
  .panel-light { fill: var(--brand-blue); }
  .panel-dark { fill: var(--brand-navy); }
  .frame { fill: none; stroke: var(--paper); stroke-width: 2.5; }
  .headline { fill: var(--paper); }
  .w-black { font-weight: 900; }
  .w-heavy { font-weight: 800; }
  .w-thin { font-weight: 200; }
  .w-medium { font-weight: 500; }
</style>
</head>
<body>
<main class="poster">
  <svg width="800" height="1200" viewBox="0 0 800 1200" xmlns="http://www.w3.org/2000/svg">
    <g class="brand">
      <circle class="brand-mark" cx="180" cy="147" r="86"/>
      <text class="brand-name" x="285" y="152" font-size="124" textLength="445" lengthAdjust="spacingAndGlyphs">WADE'S</text>
      <text class="brand-name" x="285" y="210" font-size="54" textLength="445" lengthAdjust="spacingAndGlyphs">CHECK CASHING</text>
    </g>

    <g class="offer">
      <rect class="panel-light" x="0" y="263" width="800" height="937"/>
      <polygon class="panel-dark" points="0,263 800,263 800,1200"/>
      <rect class="frame" x="71" y="346" width="654" height="766"/>

      <text class="headline w-black" x="129" y="510" font-size="166" textLength="545" lengthAdjust="spacingAndGlyphs">LOANS</text>
      <text class="headline w-thin" x="129" y="683" font-size="206" textLength="545" lengthAdjust="spacingAndGlyphs">CASH</text>
      <text class="headline w-heavy" x="129" y="773" font-size="86" textLength="545" lengthAdjust="spacingAndGlyphs">$100 – $1,400</text>
      <text class="headline w-medium" x="129" y="849" font-size="66" textLength="545" lengthAdjust="spacingAndGlyphs">CREDIT BUILDING</text>
      <text class="headline w-black" x="129" y="997" font-size="170" textLength="545" lengthAdjust="spacingAndGlyphs">QUICK</text>
      <text class="headline w-medium" x="129" y="1063" font-size="56" textLength="545" lengthAdjust="spacingAndGlyphs">MONTHLY PAYMENTS</text>
    </g>
  </svg>
</main>
</body>
</html>
```